Refresh our business cards

Our client is an online store and requires a business card refresh

The guideline and visual identity of this brand;
1. Typography - bold
2. Key Colours - Blue and white with a touch of black as per the logo
3. Brand Elements - minimalistic and simple

Visual Identity
1. Logo - we have attached the current logo but open to suggested improvements
2. Business Cards: will include
logo, company address, email, name, facebook handle, instagram handle, twitter handle, website.

note all material, once accepted, needs to be in usable format.

WE REQUIRE A VERY GOOD RESULTS THAT CONSIDERS ALL THE ITEMS WE REQUIRE.
The business card needs to be editable so we can add other employee names to the card as required.

File format required are: ai, esp, jpg, png, pdf,

```html
<!DOCTYPE html>
<html lang="en">
<head>
<meta charset="utf-8">
<title>Blue Locket Store Online – Business Cards</title>
<link rel="stylesheet" href="https://fonts.googleapis.com/css2?family=Lato:wght@300;400;700&display=swap">
<style>
  :root{
    --bg:#e6e9ed;
    --white:#ffffff;
    --brand-blue:#3f7db8;
    --row-blue:#3a78b5;
    --cell-blue:#2c6197;
    --back-blue:#3e7fb6;
    --teal:#27a3b3;
    --ink:#2b2f36;
    --faint:rgba(255,255,255,.35);
  }
  *{box-sizing:border-box;margin:0;padding:0}
  html,body{width:1200px;height:900px;overflow:hidden;background:var(--bg);font-family:"Lato",sans-serif}
  .stage{position:relative;width:1200px;height:900px}
  .card{position:absolute;top:295px;width:540px;height:310px;border-radius:22px;overflow:hidden;box-shadow:0 10px 28px rgba(0,0,0,.18)}
  .card--front{left:50px;background:var(--white)}
  .card--back{left:610px;background:var(--back-blue)}

  .brand{position:absolute;width:150px;height:150px;display:flex;align-items:center;justify-content:center;text-align:center}
  .brand__ring{position:absolute;inset:0}
  .brand__name{position:relative;font-weight:400;font-size:15px;line-height:1.25;letter-spacing:1px;text-transform:uppercase}
  .card--front .brand{left:30px;top:40px}
  .card--front .brand__name{color:var(--brand-blue)}
  .card--back .brand{left:40px;top:40px}
  .card--back .brand__name{color:var(--white)}

  .person{position:absolute;left:232px;top:40px;color:var(--brand-blue)}
  .person__name{font-size:32px;font-weight:400;line-height:1}
  .person__title{font-size:13px;margin-top:6px;color:var(--brand-blue)}

  .contacts{position:absolute;left:208px;top:120px;right:0;list-style:none}
  .contact{display:flex;align-items:center;height:30px;margin-bottom:5px;background:var(--row-blue);color:var(--white);font-size:13px}
  .contact__icon{width:34px;height:30px;background:var(--cell-blue);display:flex;align-items:center;justify-content:center;margin-right:10px;flex:none}
  .contact__text{white-space:nowrap}

  .back__website{position:absolute;left:40px;bottom:34px;color:var(--white);font-size:17px;letter-spacing:.5px}
  .back__figure{position:absolute;left:250px;top:95px;width:95px;height:175px;border-radius:40px 40px 10px 10px;background:linear-gradient(180deg,#3ab3c1,var(--teal))}
  .back__mark{position:absolute;right:40px;top:110px;width:110px;height:110px;display:flex;align-items:center;justify-content:center;text-align:center;color:var(--faint);font-size:10px;letter-spacing:1px;text-transform:uppercase;line-height:1.3}
  .back__mark svg{position:absolute;inset:0}
</style>
</head>
<body>
<main class="stage">

  <section class="card card--front" aria-label="Business card front">
    <div class="brand">
      <svg class="brand__ring" viewBox="0 0 150 150"><circle cx="75" cy="75" r="72" fill="none" stroke="var(--brand-blue)" stroke-width="2"/></svg>
      <span class="brand__name">Blue<br>Locket<br>Store<br>Online</span>
    </div>

    <div class="person">
      <div class="person__name">Elena Varsano</div>
      <div class="person__title">Creative Managing Director</div>
    </div>

    <ul class="contacts">
      <li class="contact">
        <span class="contact__icon">
          <svg width="16" height="16" viewBox="0 0 24 24"><path fill="#fff" d="M6.6 10.8a15.1 15.1 0 0 0 6.6 6.6l2.2-2.2a1 1 0 0 1 1-.25 11.4 11.4 0 0 0 3.6.57 1 1 0 0 1 1 1V20a1 1 0 0 1-1 1A17 17 0 0 1 3 4a1 1 0 0 1 1-1h3.5a1 1 0 0 1 1 1c0 1.25.2 2.45.57 3.57a1 1 0 0 1-.25 1z"/></svg>
        </span>
        <span class="contact__text">+61 3000 4821 &nbsp;|&nbsp; +61 400 512 377</span>
      </li>
      <li class="contact">
        <span class="contact__icon">
          <svg width="18" height="14" viewBox="0 0 24 18"><rect x="1" y="1" width="22" height="16" fill="none" stroke="#fff" stroke-width="2"/><path d="M1 1l11 9 11-9" fill="none" stroke="#fff" stroke-width="2"/></svg>
        </span>
        <span class="contact__text">elena@bluelocketstore.com.au</span>
      </li>
      <li class="contact">
        <span class="contact__icon"><svg width="14" height="14"><rect width="14" height="14" fill="#fff"/></svg></span>
        <span class="contact__text">bluelocket_store_online</span>
      </li>
      <li class="contact">
        <span class="contact__icon"><svg width="14" height="14"><rect width="14" height="14" fill="#fff"/></svg></span>
        <span class="contact__text">bluelocketstore.com.au</span>
      </li>
      <li class="contact">
        <span class="contact__icon"><svg width="14" height="14"><rect width="14" height="14" fill="#fff"/></svg></span>
        <span class="contact__text">@bluelocket_au</span>
      </li>
    </ul>
  </section>

  <section class="card card--back" aria-label="Business card back">
    <div class="brand">
      <svg class="brand__ring" viewBox="0 0 150 150"><circle cx="75" cy="75" r="72" fill="none" stroke="var(--white)" stroke-width="2"/></svg>
      <span class="brand__name">Blue<br>Locket<br>Store<br>Online</span>
    </div>

    <div class="back__figure" role="img" aria-label="Illustration of a woman in a long dress"></div>

    <div class="back__mark">
      <svg viewBox="0 0 110 110"><circle cx="55" cy="55" r="53" fill="none" stroke="var(--faint)" stroke-width="1.5"/></svg>
      <span>Blue<br>Locket<br>Store</span>
    </div>

    <div class="back__website">www.bluelocketstore.com.au</div>
  </section>

</main>
</body>
</html>
```